Authentic Log Lodge Requires Highway Signage (x2)

We are recently established Lodge and Cabins in Golden, BC, Canada. We already have a great reputation and have recently achieved a Wander Ledger Badge of Distinction - our guests love us and we love them.

Tamsworth Lodge is looking for two new signs;
1 - A highway sign (8ft high, 12ft wide) and a secondary directional sign (approx 3ft square). We have a strong brand and imagery and can supply photos and vectors. We are currently fighting an internal battle of how the highway sign should look - one option includes an image of the Lodge and the other is based around our logo. The design must include two items of text - "www.tamsworthlodge.example" and "Next Right"

2 - A directional sign. We would like this sign to be logo based and include a right facing arrow. The size of this sign can be flexible.

It would be great to establish a relationship with someone for future work.

We are in desperate need of some creative geniuses to don their superhero capes and come to our rescue.

Target Market(s)

Current guests looking to find us and prospective guests driving along the highway.

Industry/Entity Type

Hospitality

Font styles to use
Sans Serif

Colors

Designer to choose colors to be used in the design.

Requirements
Must have
• It must contain our logo and maintain the feel of our brand.
• It must be based on the brand colours (see attached documents).

```html
<!DOCTYPE html>
<html lang="en">
<head>
<meta charset="utf-8">
<title>Tamsworth Lodge – Highway and Directional Signs</title>
<link rel="stylesheet" href="https://fonts.googleapis.com/css2?family=Montserrat:wght@600;700&family=Merriweather:ital,wght@1,400&display=swap">
<style>
  :root {
    --stage: #c4c4c4;
    --ink: #222222;
    --olive: #8f9444;
    --olive-band: #8e8c4a;
    --olive-light: #b7ba5a;
    --paper: #ecebd6;
    --paper-light: #f7f6ec;
    --type-light: #ececec;
  }
  * { box-sizing: border-box; margin: 0; padding: 0; }
  html, body { width: 1038px; height: 1200px; overflow: hidden; }
  body {
    background: var(--stage);
    position: relative;
    font-family: "Montserrat", Arial, sans-serif;
  }
  .sign {
    position: absolute;
    overflow: hidden;
    box-shadow: 0 8px 18px rgba(0,0,0,.28);
    background: var(--paper);
  }
  .sign--highway { left: 34px; width: 744px; height: 496px; }
  .sign--direction { left: 816px; width: 186px; height: 186px; }
  .sign--lodge-photo { top: 34px; }
  .sign--logo-led { top: 665px; }

  .scene {
    position: absolute; left: 0; top: 0; width: 100%;
    background: linear-gradient(180deg, var(--paper-light) 0%, var(--paper) 55%, #ddd9bb 100%);
  }
  .sign--lodge-photo.sign--highway .scene { height: 344px; }
  .sign--logo-led.sign--highway .scene { height: 392px; }
  .sign--direction .scene { height: 143px; }

  .lodge-name {
    position: absolute; left: 0; width: 100%;
    text-align: center;
    font-weight: 700;
    letter-spacing: .16em;
    line-height: 1.15;
  }
  .sign--highway .lodge-name { font-size: 46px; top: 120px; }
  .sign--direction .lodge-name { font-size: 15px; top: 48px; }
  .lodge-name--olive { color: var(--olive); }
  .lodge-name--dark { color: var(--ink); }

  .band {
    position: absolute; left: 0; bottom: 0; width: 100%;
    display: flex; flex-direction: column; align-items: center; justify-content: center;
  }
  .band--dark { background: var(--ink); }
  .band--olive { background: var(--olive-band); }
  .sign--lodge-photo.sign--highway .band { height: 152px; }
  .sign--logo-led.sign--highway .band { height: 104px; }
  .sign--direction .band { height: 43px; }

  .next-right {
    color: var(--type-light);
    font-weight: 600;
    font-size: 70px;
    letter-spacing: .2em;
    margin-right: -.2em;
    line-height: 1;
  }
  .web-address {
    font-family: "Merriweather", Georgia, serif;
    font-style: italic;
    font-size: 25px;
    letter-spacing: .12em;
  }
  .band .web-address { color: var(--olive-light); margin-top: 22px; }
  .web-address--on-scene {
    position: absolute; top: 340px; left: 0; width: 100%;
    text-align: center; color: var(--ink);
  }
  .chevrons { display: block; width: 186px; height: 43px; }
</style>
</head>
<body>

  <section class="sign sign--highway sign--lodge-photo">
    <div class="scene" role="img" aria-label="Softly tinted photograph of the log lodge among tall evergreens"></div>
    <div class="lodge-name lodge-name--olive">TAMSWORTH<br>LODGE</div>
    <div class="band band--dark">
      <div class="next-right">NEXT RIGHT</div>
      <div class="web-address">www.tamsworthlodge.example</div>
    </div>
  </section>

  <section class="sign sign--direction sign--lodge-photo">
    <div class="scene" role="img" aria-label="Softly tinted photograph of the log lodge"></div>
    <div class="lodge-name lodge-name--olive">TAMSWORTH<br>LODGE</div>
    <div class="band band--dark">
      <svg class="chevrons" viewBox="0 0 186 43" aria-label="Arrow pointing right">
        <g fill="none" stroke-width="6" stroke-linecap="square">
          <path d="M12 10 L22 21.5 L12 33" stroke="#4d4e34"/>
          <path d="M47 10 L57 21.5 L47 33" stroke="#66683c"/>
          <path d="M82 10 L92 21.5 L82 33" stroke="#868a45"/>
          <path d="M117 10 L127 21.5 L117 33" stroke="#a2a64e"/>
          <path d="M152 10 L162 21.5 L152 33" stroke="#c2c560"/>
        </g>
      </svg>
    </div>
  </section>

  <section class="sign sign--highway sign--logo-led">
    <div class="scene" role="img" aria-label="Softly tinted photograph of the log lodge among tall evergreens"></div>
    <div class="lodge-name lodge-name--dark">TAMSWORTH<br>LODGE</div>
    <div class="web-address web-address--on-scene">www.tamsworthlodge.example</div>
    <div class="band band--olive">
      <div class="next-right">NEXT RIGHT</div>
    </div>
  </section>

  <section class="sign sign--direction sign--logo-led">
    <div class="scene" role="img" aria-label="Softly tinted photograph of the log lodge"></div>
    <div class="lodge-name lodge-name--dark">TAMSWORTH<br>LODGE</div>
    <div class="band band--olive">
      <svg class="chevrons" viewBox="0 0 186 43" aria-label="Arrow pointing right">
        <g fill="none" stroke-width="6" stroke-linecap="square">
          <path d="M12 10 L22 21.5 L12 33" stroke="#a3a26a"/>
          <path d="M47 10 L57 21.5 L47 33" stroke="#b7b68a"/>
          <path d="M82 10 L92 21.5 L82 33" stroke="#cbcaa8"/>
          <path d="M117 10 L127 21.5 L117 33" stroke="#e0dfcb"/>
          <path d="M152 10 L162 21.5 L152 33" stroke="#f4f4ee"/>
        </g>
      </svg>
    </div>
  </section>

</body>
</html>
```